Quran Jar

So I need help designing bespoke jars which will contain religious quotes.

So there will be three jars in total sold either individually or in two or as a three.

Each Jar will have different contents and preferably a different colour scheme.

I want the packaging to be customised with my branding and logo and to make the product stand out I am thinking of packing it further in a cotton bag with my branding.

```html
<!DOCTYPE html>
<html lang="en">
<head>
<meta charset="utf-8">
<title>Quran Jar – Label</title>
<link href="https://fonts.googleapis.com/css2?family=Montserrat:wght@300;400;600;800&family=Arimo:wght@400;500&display=swap" rel="stylesheet">
<style>
  :root{
    --green-bg:#0e4423;
    --green-deep:#063a1b;
    --green-ink:#0b4a22;
    --gold:#e6cc7f;
    --gold-light:#f6e29a;
    --gold-dark:#c9a44c;
    --white:#ffffff;
    --ink:#1c1c1c;
    --book-top:#d9c9a0;
    --book-bottom:#a9763f;
    --star-happy:#9acd32;
    --star-sad:#2e3192;
    --star-angry:#ed1c24;
    --star-anxious:#f7821e;
    --star-lonely:#92278f;
    --star-thankful:#0095da;
  }
  *{margin:0;padding:0;box-sizing:border-box}
  html,body{width:1200px;height:1067px;overflow:hidden;background:var(--green-bg)}
  .label{position:relative;width:1200px;height:1067px;background:var(--green-bg);font-family:'Montserrat',sans-serif;color:var(--white)}
  .corner{position:absolute;top:62px;width:177px;height:178px;background:linear-gradient(135deg,rgba(230,204,127,.55),rgba(230,204,127,.15));clip-path:polygon(0 0,100% 0,0 100%)}
  .corner--left{left:58px}
  .corner--right{right:58px;transform:scaleX(-1)}
  .brand-box{position:absolute;left:340px;top:62px;width:520px;height:255px;background:var(--green-deep);text-align:center}
  .brand-name{position:absolute;left:0;right:0;top:162px;font-weight:600;font-size:56px;line-height:1;color:var(--gold);display:flex;align-items:center;justify-content:center;gap:14px}
  .brand-dot{width:18px;height:18px;border-radius:50%;background:var(--gold)}
  .brand-tagline{position:absolute;left:0;right:0;top:231px;font-size:11px;font-weight:600;letter-spacing:5px;color:var(--gold)}
  .title{position:absolute;left:0;right:0;top:322px;text-align:center;font-weight:800;font-size:124px;line-height:1.1;letter-spacing:0}
  .subtitle{position:absolute;left:0;right:0;top:452px;text-align:center;font-weight:400;font-size:33px;letter-spacing:7.5px;padding-left:7px}
  .tab{position:absolute;left:315px;top:496px;width:570px;height:66px}
  .tab-text{position:absolute;left:315px;top:497px;width:570px;text-align:center;font-weight:800;font-size:58px;line-height:66px;color:var(--green-ink);letter-spacing:-1px}
  .banner{position:absolute;left:49px;top:561px;width:1102px;height:287px}
  .emotions{position:absolute;list-style:none;font-family:'Arimo',sans-serif;font-size:56px;color:var(--ink)}
  .emotions li{display:flex;align-items:center;height:79.5px}
  .emotions svg{width:54px;height:54px;margin-right:20px}
  .emotions--left{left:157px;top:588px}
  .emotions--right{left:692px;top:588px}
  .book{position:absolute;left:425px;top:620px;width:240px;height:180px;border-radius:12px;background:linear-gradient(180deg,var(--book-top),var(--book-bottom))}
  .verses{position:absolute;left:0;right:0;top:862px;text-align:center;font-family:'Arimo',sans-serif;font-weight:500;font-size:58px;line-height:1.1;color:var(--gold);letter-spacing:-.3px}
  .quote{position:absolute;left:0;right:0;top:937px;text-align:center;font-family:'Arimo',sans-serif;font-size:25px;line-height:31px}
</style>
</head>
<body>
<div class="label">
  <div class="corner corner--left" role="img" aria-label="Gold filigree corner ornament"></div>
  <div class="corner corner--right" role="img" aria-label="Gold filigree corner ornament"></div>

  <div class="brand-box">
    <div class="brand-name"><span class="brand-dot"></span>Noor Pages</div>
    <div class="brand-tagline">WORDS OF LIGHT FOR EVERY DAY</div>
  </div>

  <h1 class="title">QURAN JAR</h1>
  <p class="subtitle">A DUA FOR EVERY EMOTION</p>

  <svg class="tab" viewBox="0 0 570 66" preserveAspectRatio="none" aria-hidden="true">
    <defs>
      <linearGradient id="goldTab" x1="0" y1="0" x2="1" y2="0">
        <stop offset="0" stop-color="#d9b960"/>
        <stop offset=".5" stop-color="#f6e29a"/>
        <stop offset="1" stop-color="#d9b960"/>
      </linearGradient>
    </defs>
    <path d="M0,66 L14,12 Q18,2 32,2 H538 Q552,2 556,12 L570,66 Z" fill="url(#goldTab)"/>
  </svg>
  <div class="tab-text">READ ME WHEN</div>

  <svg class="banner" viewBox="0 0 1102 287" aria-hidden="true">
    <path d="M95,4 H1007 C1007,40 1032,58 1056,68 C1060,110 1096,128 1096,143 C1096,158 1060,176 1056,218 C1032,228 1007,246 1007,283 H95 C95,246 70,228 46,218 C42,176 6,158 6,143 C6,128 42,110 46,68 C70,58 95,40 95,4 Z" fill="var(--white)" stroke="var(--gold)" stroke-width="7"/>
  </svg>

  <ul class="emotions emotions--left">
    <li><svg viewBox="0 0 24 24"><polygon points="12,1 15,9 23.5,9.2 16.8,14.4 19.2,22.8 12,17.9 4.8,22.8 7.2,14.4 0.5,9.2 9,9" fill="var(--star-happy)"/></svg>HAPPY</li>
    <li><svg viewBox="0 0 24 24"><polygon points="12,1 15,9 23.5,9.2 16.8,14.4 19.2,22.8 12,17.9 4.8,22.8 7.2,14.4 0.5,9.2 9,9" fill="var(--star-sad)"/></svg>SAD</li>
    <li><svg viewBox="0 0 24 24"><polygon points="12,1 15,9 23.5,9.2 16.8,14.4 19.2,22.8 12,17.9 4.8,22.8 7.2,14.4 0.5,9.2 9,9" fill="var(--star-angry)"/></svg>ANGRY</li>
  </ul>

  <div class="book" role="img" aria-label="Illustration of an open Quran resting on a wooden stand"></div>

  <ul class="emotions emotions--right">
    <li><svg viewBox="0 0 24 24"><polygon points="12,1 15,9 23.5,9.2 16.8,14.4 19.2,22.8 12,17.9 4.8,22.8 7.2,14.4 0.5,9.2 9,9" fill="var(--star-anxious)"/></svg>ANXIOUS</li>
    <li><svg viewBox="0 0 24 24"><polygon points="12,1 15,9 23.5,9.2 16.8,14.4 19.2,22.8 12,17.9 4.8,22.8 7.2,14.4 0.5,9.2 9,9" fill="var(--star-lonely)"/></svg>LONELY</li>
    <li><svg viewBox="0 0 24 24"><polygon points="12,1 15,9 23.5,9.2 16.8,14.4 19.2,22.8 12,17.9 4.8,22.8 7.2,14.4 0.5,9.2 9,9" fill="var(--star-thankful)"/></svg>THANKFUL</li>
  </ul>

  <h2 class="verses">COLOUR CODED QURAN VERSES</h2>
  <p class="quote">"Do you not see how Allah compares a good word to a good tree?<br>Its root is firm and its branches reach the sky."<br>(Surah Ibrahim 14:24).</p>
</div>
</body>
</html>
```